Netvale - Seafood industry professional promoting page

Hi. I´m in the seafood business with a one man company sourcing and exporting frozen seafood. I need to make a one page homepage for Netvale (from Iceland). The feeling of it should be; Trustworthy, experience and knowledge.
Using as background a picture (or part of it), or a moving video:

http://www1.bryla.is/vefur/myndir/lysingur.jpg
https://clipvault.example/583027416

Main text to be:

- We can help source, market and add value to your seafood business
- Years of experience in seafood trade and production
- Extensive knowledge of fishing, seasonality, production and accreditations

Contact:
torvi@netvale.is
Tel: +3654172093
(with a photo)

p.s. please also make logo look better.

Target Market(s)

Seafood industry

Industry/Entity Type

Business

Logo Text

Netvale

Coding

Coded - Design and coding required

Number of Pages Required

1 page

Colors
0792cd
33a6d7

```html
<!DOCTYPE html>
<html lang="en">
<head>
<meta charset="utf-8">
<title>Netvale – Frozen Seafood Export</title>
<link href="https://fonts.googleapis.com/css2?family=Open+Sans:wght@400;600;700&family=Arimo:wght@400;700&display=swap" rel="stylesheet">
<style>
:root{
  --blue:#0792cd;
  --blue-light:#33a6d7;
  --ink:#333;
  --muted:#555;
  --light-bg:#f0f0f0;
  --footer-bg:#262626;
  --footer-text:#d8d8d8;
  --footer-muted:#9a9a9a;
  --line:#dcdcdc;
}
*{margin:0;padding:0;box-sizing:border-box}
html,body{width:683px;height:1200px;overflow:hidden;background:#fff}
body{position:relative;font-family:"Open Sans",sans-serif;color:var(--ink)}
.abs{position:absolute}

/* hero */
.hero{left:0;top:74px;width:683px;height:292px;
  background:
    radial-gradient(ellipse 180px 90px at 560px 290px,#b8503f 0%,rgba(184,80,63,0) 100%),
    radial-gradient(ellipse 160px 80px at 170px 200px,#9a6a66 0%,rgba(154,106,102,0) 100%),
    radial-gradient(ellipse 220px 70px at 420px 170px,#5f6a72 0%,rgba(95,106,114,0) 100%),
    linear-gradient(120deg,#6d747a 0%,#a9b1b6 35%,#868f95 55%,#9c5a50 80%,#5e4644 100%)}
.play{left:320px;top:197px}
.hero-points{left:38px;top:302px;list-style:none;padding:9px 14px 9px 12px;background:rgba(20,40,55,.55);border-left:3px solid var(--blue-light)}
.hero-points li{font-size:10px;line-height:17px;color:#fff;display:flex;align-items:center;gap:7px;font-weight:600}

/* header */
.brand{left:38px;top:26px;display:flex;align-items:center;gap:6px}
.brand-dot{width:12px;height:12px;border-radius:50%;background:var(--blue)}
.brand-name{font-size:22px;font-weight:700;color:var(--blue);letter-spacing:.5px}
.contact-item{top:18px;display:flex;gap:6px;align-items:flex-start}
.contact-item svg{margin-top:3px}
.contact-label{font-size:11px;font-weight:700;color:#333;letter-spacing:.4px;line-height:13px}
.contact-value{font-size:9px;color:#555;line-height:13px}

.nav{left:38px;top:62px;width:608px;height:27px;background:var(--blue);display:flex;justify-content:space-between;padding:0 12px}
.nav a{color:#fff;text-decoration:none;font-size:8.6px;line-height:27px;position:relative}
.nav a.active::after{content:"";position:absolute;left:0;right:0;bottom:0;height:2px;background:#fff}

/* intro */
.intro-title{left:0;width:683px;top:390px;text-align:center;font-size:19px;font-weight:400;color:#444;letter-spacing:.3px}
.intro-sub{left:0;width:683px;top:412px;text-align:center;font-size:10px;color:#666}
.service{top:444px;height:173px;border:1px solid var(--line);background:#fff;text-align:center}
.service .photo{height:96px}
.service h3{font-size:8.3px;font-weight:600;margin-top:9px;letter-spacing:.3px;color:#333}
.service p{font-family:"Arimo",sans-serif;font-size:7.4px;line-height:10.5px;color:#555;margin:4px 12px 0}

/* products */
.products{left:0;top:641px;width:683px;height:367px;background:var(--light-bg)}
.products-title{left:0;width:683px;top:658px;text-align:center;font-size:19px;font-weight:600;color:#333;letter-spacing:.5px}
.dots{left:331px;top:690px;display:flex;gap:3px}
.dots span{width:5px;height:5px;border-radius:50%;background:var(--blue)}
.product{width:183px;height:122px}
.product-hover{position:absolute;inset:0;background:rgba(30,34,38,.55)}
.product-frame{position:absolute;left:6px;top:6px;right:6px;bottom:6px;border:1px solid rgba(255,255,255,.7)}
.view-btn{position:absolute;left:54px;top:81px;width:74px;height:21px;border:1.5px solid #fff;color:#fff;font-size:8.5px;font-weight:600;letter-spacing:.8px;text-align:center;line-height:18px}
.zoom{position:absolute;left:82px;top:44px}

/* footer */
.footer{left:0;top:1008px;width:683px;height:192px;background:var(--footer-bg)}
.f-text{font-family:"Arimo",sans-serif}
.f-head{top:1029px;font-size:11.5px;font-weight:700;color:#fff}
.f-head::after{content:"";display:block;width:42px;height:1px;background:#444;margin-top:5px}
.f-brand{left:47px;top:1062px;display:flex;align-items:center;gap:5px}
.f-brand .brand-dot{background:#8a8a8a;width:10px;height:10px}
.f-brand span{font-size:17px;font-weight:700;color:#8a8a8a}
.f-info{left:48px;font-size:7.4px;color:var(--footer-muted);display:flex;gap:5px;align-items:center}
.f-info.bright{color:var(--footer-text)}
.f-links{left:263px;top:1059px;list-style:none}
.f-links li{font-size:7.4px;color:var(--footer-text);line-height:15.2px;display:flex;align-items:center;gap:4px}
.f-links li::before{content:"";border-left:3px solid var(--blue-light);border-top:2.5px solid transparent;border-bottom:2.5px solid transparent}
.subscribe{left:455px;top:1066px;width:183px;height:22px;display:flex}
.subscribe .field{flex:1;background:#fff}
.subscribe .send{width:32px;background:#6a6a6a;display:flex;align-items:center;justify-content:center}
.f-note{left:455px;top:1096px;font-size:7.4px;color:var(--footer-muted)}
.f-rule{left:455px;top:1118px;width:183px;height:1px;background:#3a3a3a}
.social{font-size:7.4px;color:var(--footer-text);display:flex;align-items:center;gap:6px}
.social i{width:5px;height:5px;background:var(--footer-text);display:inline-block}
.bottom-rule{left:15px;top:1176px;width:653px;height:1px;background:#3a3a3a}
.copyright{left:0;width:683px;top:1183px;text-align:center;font-size:7.6px;color:var(--footer-text)}
</style>
</head>
<body>

<section>
  <div class="abs hero" role="img" aria-label="Video still of fresh fish, octopus and clams laid on crushed ice"></div>
  <svg class="abs play" width="45" height="45" viewBox="0 0 45 45"><circle cx="22.5" cy="22.5" r="22" fill="rgba(255,255,255,.75)"/><path d="M17 12l16 10.5L17 33z" fill="#666"/></svg>
  <ul class="abs hero-points">
    <li><svg width="9" height="8" viewBox="0 0 9 8"><path d="M1 4.2l2.3 2.3L8 1.2" fill="none" stroke="#33a6d7" stroke-width="1.6"/></svg>We can help source, market and add value to your seafood business</li>
    <li><svg width="9" height="8" viewBox="0 0 9 8"><path d="M1 4.2l2.3 2.3L8 1.2" fill="none" stroke="#33a6d7" stroke-width="1.6"/></svg>Years of experience in seafood trade and production</li>
    <li><svg width="9" height="8" viewBox="0 0 9 8"><path d="M1 4.2l2.3 2.3L8 1.2" fill="none" stroke="#33a6d7" stroke-width="1.6"/></svg>Extensive knowledge of fishing, seasonality, production and accreditations</li>
  </ul>
</section>

<header>
  <div class="abs brand"><span class="brand-dot"></span><span class="brand-name">NETVALE</span></div>

  <div class="abs contact-item" style="left:470px">
    <svg width="11" height="14" viewBox="0 0 11 14"><path d="M5.5 0C2.5 0 0 2.4 0 5.4 0 9.2 5.5 14 5.5 14S11 9.2 11 5.4C11 2.4 8.5 0 5.5 0zm0 7.4a2 2 0 1 1 0-4 2 2 0 0 1 0 4z" fill="#222"/></svg>
    <div><div class="contact-label">ADDRESS</div><div class="contact-value">torvi@netvale.is</div></div>
  </div>
  <div class="abs contact-item" style="left:573px">
    <svg width="15" height="15" viewBox="0 0 16 16"><circle cx="8" cy="8" r="7.2" fill="none" stroke="#222" stroke-width="1.2"/><path d="M5.2 4.2l1.4-.2.9 2-.9.8c.5 1 1.2 1.8 2.2 2.3l.8-.9 2 .9-.2 1.4c-3.4.3-6.5-2.8-6.2-6.3z" fill="#222"/></svg>
    <div><div class="contact-label">CALL US</div><div class="contact-value">+3654172093</div></div>
  </div>

  <nav class="abs nav">
    <a class="active" href="#">HOME</a><a href="#">ABOUT US</a><a href="#">OUR PRODUCTS</a><a href="#">TIDEHOUSE</a><a href="#">SEACARRY</a><a href="#">TRACEABILITY</a><a href="#">CONTACT US</a>
  </nav>
</header>

<section>
  <h1 class="abs intro-title">BEST EXPORTING FROZEN SEAFOOD.</h1>
  <p class="abs intro-sub">Supplying Restaurants, Retail Stores and Wholesale Businesses all around the world</p>

  <div class="abs service" style="left:50px;width:130px">
    <div class="photo" role="img" aria-label="Mackerel on ice" style="background:linear-gradient(135deg,#c9d6e4,#6f7f92)"></div>
    <h3>SEAFOOD TRADING</h3><p>A refined center console for serious fishermen and their families.</p>
  </div>
  <div class="abs service" style="left:198px;width:134px">
    <div class="photo" role="img" aria-label="Whole fish with lemons and herbs" style="background:linear-gradient(135deg,#d7d0c8,#9b7f7a 60%,#b43a3a)"></div>
    <h3>SEAFOOD IMPORT</h3><p>A refined center console for serious fishermen and their families.</p>
  </div>
  <div class="abs service" style="left:349px;width:133px">
    <div class="photo" role="img" aria-label="Mixed seafood display with octopus and lobster" style="background:linear-gradient(135deg,#b7b3ae,#7a5a5a 55%,#c24a3a)"></div>
    <h3>SEAFOOD EXPORT</h3><p>A refined center console for serious fishermen and their families.</p>
  </div>
  <div class="abs service" style="left:499px;width:133px">
    <div class="photo" role="img" aria-label="Red fish on ice with lemons" style="background:linear-gradient(135deg,#e4e1e0,#d98a80 60%,#c9645a)"></div>
    <h3>FROZEN SEAFOOD</h3><p>A refined center console for serious fishermen and their families.</p>
  </div>
</section>

<section>
  <div class="abs products"></div>
  <h2 class="abs products-title">OUR PRODUCTS</h2>
  <div class="abs dots"><span></span><span></span><span></span></div>

  <div class="abs product" style="left:54px;top:713px;background:linear-gradient(135deg,#8e949a,#4a5056)" role="img" aria-label="Mackerel with lemon">
    <div class="product-hover"></div><div class="product-frame"></div>
    <svg class="zoom" width="18" height="18" viewBox="0 0 18 18"><circle cx="10.5" cy="7.5" r="5.5" fill="none" stroke="#fff" stroke-width="1.6"/><path d="M6.5 11.5L1.5 16.5" stroke="#fff" stroke-width="2"/><path d="M10.5 5v5M8 7.5h5" stroke="#fff" stroke-width="1.4"/></svg>
    <div class="view-btn">VIEW NOW</div>
  </div>
  <div class="abs product" style="left:252px;top:713px;background:linear-gradient(135deg,#9ba57a,#8a8a86 50%,#5f6468)" role="img" aria-label="Raw prawns on a board"></div>
  <div class="abs product" style="left:449px;top:713px;background:linear-gradient(135deg,#5a3a2a,#d89a4a 50%,#e8e4dc)" role="img" aria-label="Seafood pasta in a white dish"></div>
  <div class="abs product" style="left:54px;top:852px;background:linear-gradient(135deg,#e8eef2,#d88a6a 45%,#8a3a2a)" role="img" aria-label="Octopus, salmon and white fish on ice"></div>
  <div class="abs product" style="left:252px;top:852px;background:linear-gradient(135deg,#3a2a22,#8a8078 50%,#c8c4be)" role="img" aria-label="Fish market display on ice"></div>
  <div class="abs product" style="left:449px;top:852px;background:linear-gradient(135deg,#2a3038,#e89070 55%,#f0c0a8)" role="img" aria-label="Plate of cooked shrimp with lemon"></div>
</section>

<footer class="f-text">
  <div class="abs footer"></div>

  <h4 class="abs f-head" style="left:47px">Contact Us</h4>
  <div class="abs f-brand"><span class="brand-dot"></span><span>NETVALE</span></div>
  <div class="abs f-info" style="top:1111px">
    <svg width="6" height="8" viewBox="0 0 11 14"><path d="M5.5 0C2.5 0 0 2.4 0 5.4 0 9.2 5.5 14 5.5 14S11 9.2 11 5.4C11 2.4 8.5 0 5.5 0z" fill="#9a9a9a"/></svg>14 Netvale Road, New york ,USA.</div>
  <div class="abs f-info" style="top:1129px">
    <svg width="7" height="7" viewBox="0 0 10 10"><path d="M1 1.5l2-.5 1.2 2.4-1 .9c.6 1.2 1.4 2 2.6 2.6l.9-1 2.4 1.2-.5 2C4.8 9.4.6 5.2 1 1.5z" fill="#9a9a9a"/></svg>+3654172093</div>
  <div class="abs f-info bright" style="top:1146px">
    <svg width="8" height="6" viewBox="0 0 10 7"><rect width="10" height="7" fill="#9a9a9a"/><path d="M0 0l5 4 5-4" fill="none" stroke="#262626" stroke-width="1"/></svg>torvi@netvale.is</div>

  <h4 class="abs f-head" style="left:263px">Explore</h4>
  <ul class="abs f-links">
    <li>Home</li><li>Blog</li><li>Online Store</li><li>Recommended Tilefish Tackle</li><li>Tilefish FAQ</li><li>Gallery</li><li>Private Coaching</li>
  </ul>

  <h4 class="abs f-head" style="left:456px">Subscribe</h4>
  <div class="abs subscribe"><div class="field"></div><div class="send">
    <svg width="11" height="8" viewBox="0 0 11 8"><rect x=".5" y=".5" width="10" height="7" fill="none" stroke="#fff"/><path d="M.5.5l5 4 5-4" fill="none" stroke="#fff"/></svg></div></div>
  <p class="abs f-note">Get Latest updates and offers.</p>
  <div class="abs f-rule"></div>
  <div class="abs social" style="left:455px;top:1131px"><i></i>Pagewall</div>
  <div class="abs social" style="left:529px;top:1131px"><i></i>Circlenet</div>
  <div class="abs social" style="left:455px;top:1150px"><i></i>Chirpline</div>
  <div class="abs social" style="left:529px;top:1149px"><i></i>Workwire</div>

  <div class="abs bottom-rule"></div>
  <p class="abs copyright">Copyright ©2017 Netvale.si. All Rights Reserved</p>
</footer>

</body>
</html>
```